Wills & Estate Planning *

I have my own logo, just looking for a nice eye catching background with good quality.

Could we find a place for 'We give you the peace of mind you deserve'
Updates

Could we find somewhere on the card to put 'We give you the peace of mind you deserve' Thanks.

Target Market(s)

40+ age

Industry/Entity Type

Law Firm

Contact Information for Business Card

Colin Maranby
01632 960581
admin@oakmerelegacy.co.uk
www.oakmerelegacy.co.uk

Requirements
Must have
• Please use my logo attached on the brief

```html
<!DOCTYPE html>
<html lang="en">
<head>
<meta charset="utf-8">
<title>Oakmere Legacy – Business Card</title>
<link rel="stylesheet" href="https://fonts.googleapis.com/css2?family=Lato:wght@400;700&display=swap">
<style>
  :root {
    --page-bg: #e4e6ea;
    --card-top: #f4f6f9;
    --card-mid: #e3e8f0;
    --card-bottom: #eceef2;
    --navy: #1e2640;
    --navy-soft: #3a4157;
    --text-grey: #4a4f5c;
    --map-tone: #b9c3d6;
    --map-edge: #d6dce8;
  }
  * { margin: 0; padding: 0; box-sizing: border-box; }
  html, body {
    width: 1200px;
    height: 970px;
    overflow: hidden;
    background: var(--page-bg);
    font-family: "Lato", Arial, sans-serif;
  }
  .business-card {
    position: absolute;
    left: 100px;
    top: 186px;
    width: 1000px;
    height: 598px;
    background:
      radial-gradient(ellipse 70% 55% at 20% 15%, rgba(255, 255, 255, 0.9), rgba(255, 255, 255, 0) 70%),
      linear-gradient(160deg, var(--card-top) 0%, var(--card-mid) 55%, var(--card-bottom) 100%);
    box-shadow: 0 10px 30px rgba(30, 38, 64, 0.15);
    overflow: hidden;
  }
  .world-map-area {
    position: absolute;
    left: 107px;
    top: 114px;
    width: 850px;
    height: 258px;
    border-radius: 60px;
    background: radial-gradient(ellipse at 55% 50%, var(--map-tone) 0%, var(--map-edge) 45%, rgba(214, 220, 232, 0) 75%);
  }
  .brand {
    position: absolute;
    left: 0;
    top: 66px;
    width: 100%;
    text-align: center;
  }
  .brand-mark {
    display: block;
    width: 100px;
    height: 100px;
    margin: 0 auto 52px;
    background: var(--navy);
  }
  .brand-name {
    font-size: 50px;
    font-weight: 400;
    letter-spacing: 3px;
    line-height: 1;
    color: var(--navy);
    text-transform: uppercase;
  }
  .tagline {
    margin-top: 18px;
    font-size: 20px;
    letter-spacing: 1px;
    color: var(--navy-soft);
  }
  .holder {
    position: absolute;
    right: 83px;
    top: 404px;
    text-align: right;
    color: var(--navy);
  }
  .holder-name {
    font-size: 26px;
    font-weight: 400;
    letter-spacing: 0.5px;
  }
  .holder-name strong { font-weight: 700; }
  .holder-role {
    margin-top: 6px;
    font-size: 20px;
    color: var(--navy-soft);
  }
  .website {
    margin-top: 26px;
    font-size: 21px;
    font-weight: 700;
    letter-spacing: 0.5px;
  }
  .contact-list {
    position: absolute;
    left: 60px;
    top: 445px;
    list-style: none;
    font-size: 20px;
    color: var(--text-grey);
  }
  .contact-list li {
    display: flex;
    align-items: center;
    gap: 16px;
    height: 38px;
  }
  .contact-icon { width: 20px; height: 20px; fill: var(--text-grey); }
  .footer-band {
    position: absolute;
    left: 0;
    bottom: 0;
    width: 100%;
    height: 20px;
    background: var(--navy);
  }
</style>
</head>
<body>
  <div class="business-card">
    <div class="world-map-area" role="img" aria-label="Faint dotted world map in soft blue-grey behind the brand name"></div>

    <div class="brand">
      <span class="brand-mark"></span>
      <div class="brand-name">Oakmere Legacy</div>
      <div class="tagline">We give you the peace of mind you deserve</div>
    </div>

    <ul class="contact-list">
      <li>
        <svg class="contact-icon" viewBox="0 0 24 24" aria-hidden="true">
          <path d="M3 9c0-3 4-5 9-5s9 2 9 5v2h-5V9c-1-.6-2.5-1-4-1s-3 .4-4 1v2H3z"/>
          <path d="M6 13h12l2 7H4z"/>
        </svg>
        <span>01632 960581</span>
      </li>
      <li>
        <svg class="contact-icon" viewBox="0 0 24 24" aria-hidden="true">
          <path d="M2 5h20v14H2z M4 7v.5l8 5.5 8-5.5V7z" fill-rule="evenodd"/>
        </svg>
        <span>admin@oakmerelegacy.co.uk</span>
      </li>
    </ul>

    <div class="holder">
      <div class="holder-name">COLIN <strong>MARANBY</strong></div>
      <div class="holder-role">Managing Director</div>
      <div class="website">www.oakmerelegacy.co.uk</div>
    </div>

    <div class="footer-band"></div>
  </div>
</body>
</html>
```